Private Investment Firm Needs PowerPoint Presentation Template

Design PowerPoint template, take Ridgeholm-submitted rough presentation draft, and drop it into new template. See attached Project Brief file for more detail.
Updates

Some decent designs have been submitted but they seem to lack the understanding of our target markets. I am hopeful that more time and feedback will result in better results.

Target Market(s)

Private company owners and intermediaries.

Font styles to use
Serif

Colors
3176b5

Requirements
Must have
• See attached Project Brief.
Nice to have
Should not have
• No B2C fluff--this is a B2B project.

```html
<!DOCTYPE html>
<html lang="en">
<head>
<meta charset="utf-8">
<title>Ridgeholm Capital – Investor Questions Deck</title>
<link rel="stylesheet" href="https://fonts.googleapis.com/css2?family=Raleway:wght@500;600;700&family=Cormorant+Garamond:wght@600&display=swap">
<style>
:root{
  --navy:#284766;
  --accent:#1f78c1;
  --title:#0b6db6;
  --ink:#3c3c3c;
  --ink-strong:#1f2f44;
  --empty:#e8e8e8;
  --page:#ffffff;
}
*{box-sizing:border-box;margin:0;padding:0}
html,body{width:1200px;height:1200px;overflow:hidden;background:var(--page)}
body{position:relative;font-family:"Raleway",Arial,sans-serif;color:var(--ink)}
.slide{position:absolute;width:397px;height:397px;background:#fff;overflow:hidden;box-shadow:0 0 0 1px #ececec}
.slide.empty{background:var(--empty);box-shadow:none}
.top-band{position:absolute;left:0;top:0;width:397px;height:24px}
.bottom-band{position:absolute;left:0;top:369px;width:300px;height:26px}
.page-no{position:absolute;top:376px;left:180px;width:40px;text-align:center;color:#fff;font-weight:700;font-size:10px}
.brand{position:absolute;top:368px;right:12px;display:flex;align-items:center;gap:4px}
.brand-dot{width:16px;height:16px;border-radius:50%;border:2px solid var(--accent)}
.brand-name{font-family:"Cormorant Garamond",Georgia,serif;font-weight:600;font-size:11px;letter-spacing:1px;color:var(--navy)}
.title{position:absolute;top:45px;left:0;width:100%;text-align:center;color:var(--title);font-weight:700;font-size:22px;line-height:22px}
.content{position:absolute;left:10px;right:10px;font-size:10.6px;line-height:13.4px;font-weight:600}
.question{color:var(--title);font-weight:700;margin-bottom:4px}
.answer{color:var(--ink);margin-bottom:8px}
.answer b{color:var(--ink-strong);font-weight:700}
.note{color:var(--ink);padding-left:9px;text-indent:-9px}
.contact-title{position:absolute;top:58px;left:0;width:100%;text-align:center;color:var(--title);font-weight:700;font-size:22px}
.contact{position:absolute;left:20px;top:97px;font-size:10.6px;line-height:13.3px;font-weight:600;color:var(--ink)}
.contact .office{color:var(--title);margin-top:0}
.contact .block{margin-bottom:7px}
.contact .email{color:var(--ink-strong);font-weight:700}
.web{display:flex;align-items:center;gap:4px;color:var(--ink-strong);font-weight:700}
.portrait{position:absolute;left:258px;top:124px;width:119px;height:186px;background:linear-gradient(180deg,#c3d3e6 0%,#b7c9de 60%,#a9bccf 100%)}
</style>
</head>
<body>

<!-- helper: shared band shapes repeated per slide -->

<section class="slide" style="left:0;top:0">
  <svg class="top-band" viewBox="0 0 397 24"><polygon points="36,0 50,0 62,12 48,12" fill="var(--accent)"/><polygon points="50,0 397,0 397,22 72,22" fill="var(--navy)"/></svg>
  <h2 class="title">The Critical Questions To Ask<br>Of Any Prospective Non-Control<br>Investor</h2>
  <div class="content" style="top:134px">
    <p class="question">Question #1: How many years has the firm been investing Non-Control Capital?</p>
    <p class="answer"><b>- Best Answer:</b> 5+ years investing as a team within the current firm</p>
    <p class="note" style="margin-bottom:26px">- Indicates comfort and experience evaluating and making NCC investments with each other and increases likelihood of close</p>
    <p class="question">Question #2: How may fully-invested Non-Control Capital funds in the firm’s history?</p>
    <p class="answer"><b>- Best Answer:</b> 2+ fully-invested funds</p>
    <p class="note">- Indicates experience and ability to close deals with the current regime—those firms without it may only be testing the waters and not have a long-term commitment to NCC investing</p>
  </div>
  <svg class="bottom-band" viewBox="0 0 300 26"><polygon points="0,2 252,2 276,26 0,26" fill="var(--navy)"/><polygon points="256,2 268,2 292,26 280,26" fill="var(--accent)"/></svg>
  <span class="page-no">20</span>
  <div class="brand"><span class="brand-dot"></span><span class="brand-name">RIDGEHOLM</span></div>
</section>

<section class="slide" style="left:402px;top:0">
  <svg class="top-band" viewBox="0 0 397 24"><polygon points="36,0 50,0 62,12 48,12" fill="var(--accent)"/><polygon points="50,0 397,0 397,22 72,22" fill="var(--navy)"/></svg>
  <h2 class="title">The Critical Questions To Ask<br>Of Any Prospective Non-Control<br>Investor</h2>
  <div class="content" style="top:134px">
    <p class="question">Question #3: What percentage of the firm’s voting investment committee are full-time Non-Control Capital investors?</p>
    <p class="answer"><b>- Best Answer:</b> Super-majority</p>
    <p class="note" style="margin-bottom:38px">- Indicates commitment, experience, and focus on NCC and overcomes dependency on buyout heritage, if any</p>
    <p class="question">Question #4: What is the number of Non-Control Capital investments made with the current firm and team?</p>
    <p class="answer"><b>- Best Answer:</b> 20+</p>
    <p class="note">- Indicates long-term experience and comfort with current team, investment committee, and NCC investment assessment</p>
  </div>
  <svg class="bottom-band" viewBox="0 0 300 26"><polygon points="0,2 252,2 276,26 0,26" fill="var(--navy)"/><polygon points="256,2 268,2 292,26 280,26" fill="var(--accent)"/></svg>
  <span class="page-no">21</span>
  <div class="brand"><span class="brand-dot"></span><span class="brand-name">RIDGEHOLM</span></div>
</section>

<section class="slide" style="left:805px;top:0">
  <svg class="top-band" viewBox="0 0 397 24"><polygon points="36,0 50,0 62,12 48,12" fill="var(--accent)"/><polygon points="50,0 397,0 397,22 72,22" fill="var(--navy)"/></svg>
  <h2 class="title">The Critical Questions To Ask<br>Of Any Prospective Non-Control<br>Investor</h2>
  <div class="content" style="top:132px">
    <p class="question">Question #5: What percentage of portfolio investments made are “sponsorless” (those without a change-of-control investor)?:</p>
    <p class="note" style="margin-bottom:13px">- Best Answer: 80%+ of all investments closed in the last 5 years (assumes current transaction is also sponsorless)</p>
    <p class="note">- I ndicates ability to add-value as a sole minority investor and not simply as a back-up to another sponsor</p>
  </div>
  <svg class="bottom-band" viewBox="0 0 300 26"><polygon points="0,2 252,2 276,26 0,26" fill="var(--navy)"/><polygon points="256,2 268,2 292,26 280,26" fill="var(--accent)"/></svg>
  <span class="page-no">22</span>
  <div class="brand"><span class="brand-dot"></span><span class="brand-name">RIDGEHOLM</span></div>
</section>

<section class="slide" style="left:0;top:402px">
  <svg class="top-band" viewBox="0 0 397 24"><polygon points="36,0 50,0 62,12 48,12" fill="var(--accent)"/><polygon points="50,0 397,0 397,22 72,22" fill="var(--navy)"/></svg>
  <h2 class="title">The Critical Questions To Ask<br>Of Any Prospective Non-Control<br>Investor</h2>
  <div class="content" style="top:142px;left:12px;right:2px">
    <p class="question" style="margin-bottom:10px">Question #6: Can the investor show quantifiable proof of their ability to assist portfolio companies with growth and improvement (assumes more than 20 exited Non-Control investments)?:</p>
    <p class="answer" style="margin-bottom:22px">- Best Answer: Yes (company owners should evaluate investors on actual historical revenue, EBITDA, and employee growth impact and the results should exceed what the current management has achieved on their own over the past 3 years)</p>
    <p class="answer">- Indicates true value-added ability to help owners grow their businesses. Those without proof of their impact, or who are unwilling to disclose it, should be excluded</p>
  </div>
  <svg class="bottom-band" viewBox="0 0 300 26"><polygon points="0,2 252,2 276,26 0,26" fill="var(--navy)"/><polygon points="256,2 268,2 292,26 280,26" fill="var(--accent)"/></svg>
  <span class="page-no">23</span>
  <div class="brand"><span class="brand-dot"></span><span class="brand-name">RIDGEHOLM</span></div>
</section>

<section class="slide" style="left:402px;top:402px">
  <svg class="top-band" viewBox="0 0 397 24"><polygon points="36,0 50,0 62,12 48,12" fill="var(--accent)"/><polygon points="50,0 397,0 397,22 72,22" fill="var(--navy)"/></svg>
  <h2 class="contact-title">Contact Us</h2>
  <div class="contact">
    <div class="block">
      <p class="office">Daniel R. Westbrook</p>
      <p>Principal</p>
      <p>41 Millbrook Avenue, Suite 210</p>
      <p>Ashford, CT&nbsp; 06278</p>
      <p>Direct: (555) 010-4412</p>
      <p class="email">dwestbrook@ridgeholmcapital.com</p>
    </div>
    <div class="block">
      <p class="office">Boston Office</p>
      <p>18 Harbor Lane, Suite 300</p>
      <p>Salem, MA 01970</p>
      <p>(555) 010-4400</p>
    </div>
    <div class="block">
      <p class="office">San Francisco Office</p>
      <p>220 Market Row, Suite 450</p>
      <p>San Francisco, CA 94105</p>
      <p>(555) 010-4600</p>
    </div>
    <p class="web"><svg width="9" height="9" viewBox="0 0 10 10" fill="none" stroke="var(--ink)" stroke-width="0.9"><circle cx="5" cy="5" r="4.2"/><ellipse cx="5" cy="5" rx="1.8" ry="4.2"/><line x1="0.8" y1="5" x2="9.2" y2="5"/></svg>www.ridgeholmcapital.com</p>
  </div>
  <div class="portrait" role="img" aria-label="Portrait photograph of the firm principal"></div>
  <svg class="bottom-band" viewBox="0 0 300 26"><polygon points="0,2 252,2 276,26 0,26" fill="var(--navy)"/><polygon points="256,2 268,2 292,26 280,26" fill="var(--accent)"/></svg>
  <span class="page-no">24</span>
  <div class="brand"><span class="brand-dot"></span><span class="brand-name">RIDGEHOLM</span></div>
</section>

<div class="slide empty" style="left:805px;top:402px"></div>
<div class="slide empty" style="left:0;top:805px"></div>
<div class="slide empty" style="left:402px;top:805px"></div>
<div class="slide empty" style="left:805px;top:805px"></div>

</body>
</html>
```